BRELLANDA EXTRA VIRGIN OLIVE OIL

I needs a design for an Australian Extra Virgin Olive Oil.

The label will go on a round clear bottle

The label size front and back is 145mm high x 60mm wide.

The important points for the design are as follows.

I want to see elegant olives on the label so that non English speaking markets can easily understand its olive oil. I want it too look classy . IT must also look Australian but I don't want to see kangaroos just colours that reflect Australia.

The mandatory info on front label will be

BRELLANDA

Cold Pressed
EXTRA VIRGIN OLIVE OIL

AUSTRALIAN

1 litre

```html
<!DOCTYPE html>
<html lang="en">
<head>
<meta charset="utf-8">
<title>Brellanda – Extra Virgin Olive Oil Label</title>
<link href="https://fonts.googleapis.com/css2?family=Ubuntu:wght@300;400;500;700&display=swap" rel="stylesheet">
<style>
  :root {
    --paper: #ffffff;
    --rule: #8a8a8a;
    --ink: #2b2b2b;
    --dim: #b8b8b8;
    --brown: #41201f;
    --brown-text: #6b4a49;
    --orange: #c85f28;
    --pale-name: #e6e2e1;
    --white: #ffffff;
    --oil-light: #e8c24a;
    --oil-deep: #a77a12;
  }
  * { box-sizing: border-box; margin: 0; padding: 0; }
  html, body { width: 1200px; height: 848px; overflow: hidden; background: var(--paper); }
  body { position: relative; font-family: "Ubuntu", sans-serif; color: var(--ink); }

  .sheet-header {
    position: absolute; left: 56px; top: 30px; width: 1080px; height: 21px;
    border-top: 1px solid var(--rule); border-bottom: 1px solid var(--rule);
    display: flex; justify-content: space-between; align-items: center;
    font-size: 12px; letter-spacing: 1.2px; text-transform: uppercase;
  }
  .sheet-footer-rule {
    position: absolute; left: 56px; top: 811px; width: 1080px;
    border-top: 1px solid var(--rule);
  }

  .dimension-width {
    position: absolute; top: 116px; height: 12px;
    border-left: 1px solid var(--dim); border-right: 1px solid var(--dim);
    border-top: 1px solid var(--dim); margin-top: 6px;
  }
  .dimension-width span {
    position: absolute; left: 50%; top: -14px; transform: translateX(-50%);
    font-size: 9px; color: var(--dim);
  }
  .dimension-height {
    position: absolute; top: 161px; height: 582px; width: 10px;
    border-top: 1px solid var(--dim); border-bottom: 1px solid var(--dim);
    border-left: 1px solid var(--dim);
  }
  .dimension-height span {
    position: absolute; left: -12px; top: 50%; transform: translateY(-50%) rotate(-90deg);
    font-size: 9px; color: var(--dim);
  }

  .label {
    position: absolute; top: 161px; width: 241px; height: 582px; text-align: center;
  }
  .label--light { background: var(--paper); border: 1px solid #d6d6d6; }
  .label--dark { background: var(--brown); }

  .label__mark {
    position: absolute; left: 50%; top: 58px; width: 44px; height: 44px;
    margin-left: -22px; border-radius: 50%;
  }
  .label--light .label__mark { background: var(--brown); }
  .label--dark .label__mark { background: var(--white); }

  .label__name {
    position: absolute; left: 0; right: 0; top: 134px;
    font-size: 29px; font-weight: 500; letter-spacing: 1px;
  }
  .label--light .label__name { color: var(--pale-name); }
  .label--dark .label__name { color: var(--white); }

  .label__method, .label__origin {
    position: absolute; left: 0; right: 0; font-weight: 300; color: var(--brown-text);
  }
  .label--dark .label__method, .label--dark .label__origin { color: #bda9a7; }
  .label__method { top: 321px; font-size: 16px; letter-spacing: 0.5px; }
  .label__origin { top: 409px; font-size: 15px; letter-spacing: 2.2px; }

  .label__band {
    position: absolute; left: 0; right: 0; top: 346px; height: 56px;
    color: var(--white); line-height: 1;
  }
  .label--light .label__band { background: var(--brown); }
  .label--dark .label__band { background: var(--orange); }
  .label__band-top { display: block; padding-top: 9px; font-size: 15px; letter-spacing: 0.5px; }
  .label__band-main { display: block; padding-top: 3px; font-size: 21px; font-weight: 700; letter-spacing: 0.5px; }

  .label__volume {
    position: absolute; left: 0; right: 0; top: 561px;
    font-size: 11px; font-weight: 300; color: var(--brown-text);
  }
  .label--dark .label__volume { color: #bda9a7; }

  .bottle-view {
    position: absolute; top: 111px; height: 634px;
    border-radius: 40px 40px 14px 14px;
    background: linear-gradient(90deg, var(--oil-deep) 0%, var(--oil-light) 35%, var(--oil-light) 60%, var(--oil-deep) 100%);
  }

  .label-tag {
    position: absolute; top: 778px; height: 16px; padding: 0 7px;
    background: var(--brown); color: var(--white); border-radius: 4px;
    font-size: 9px; line-height: 16px; transform: translateX(-50%);
  }
</style>
</head>
<body>
  <header class="sheet-header">
    <span>BRELLANDA &nbsp;|&nbsp; Extra Virgin Oil Label - 145x60 mm</span>
    <span>27.Feb.2013</span>
  </header>

  <div class="dimension-width" style="left:98px;width:241px"><span>60</span></div>
  <div class="dimension-height" style="left:62px"><span>145</span></div>

  <section class="label label--light" style="left:98px">
    <div class="label__mark"></div>
    <div class="label__name">BRELLANDA</div>
    <div class="label__method">COLD PRESSED</div>
    <div class="label__band">
      <span class="label__band-top">EXTRA VIRGIN</span>
      <span class="label__band-main">OLIVE OIL</span>
    </div>
    <div class="label__origin">AUSTRALIAN</div>
    <div class="label__volume">1 litre</div>
  </section>

  <div class="bottle-view" style="left:400px;width:136px" role="img" aria-label="Clear oil bottle wearing the white label design"></div>

  <div class="dimension-width" style="left:701px;width:241px"><span>60</span></div>
  <div class="dimension-height" style="left:664px"><span>145</span></div>

  <section class="label label--dark" style="left:701px">
    <div class="label__mark"></div>
    <div class="label__name">BRELLANDA</div>
    <div class="label__method">COLD PRESSED</div>
    <div class="label__band">
      <span class="label__band-top">EXTRA VIRGIN</span>
      <span class="label__band-main">OLIVE OIL</span>
    </div>
    <div class="label__origin">AUSTRALIAN</div>
    <div class="label__volume">1 litre</div>
  </section>

  <div class="bottle-view" style="left:1004px;width:134px" role="img" aria-label="Clear oil bottle wearing the brown label design"></div>

  <div class="label-tag" style="left:219px">Label 7</div>
  <div class="label-tag" style="left:823px">Label 8</div>

  <div class="sheet-footer-rule"></div>
</body>
</html>
```